Marine & Offshore company business card

We need a new logo design for a new company based in Singapore called "Bovenco Global Pte. Ltd.". We are suppliers of electrical items to marine and offshore industry. We specialise in lightings, cables terminations and junction box customisation. We would like the name card to have simple modern classic look.

Target Market(s)

my target customers are ship owners, shipyard purchasers, offshore purchasers.

Industry/Entity Type

Electrical

Font styles to use
Serif
Sans Serif

Colors

Designer to choose colors to be used in the design.

```html
<!DOCTYPE html>
<html lang="en">
<head>
<meta charset="utf-8">
<title>Bovenco Global Pte. Ltd. – Business Card</title>
<link href="https://fonts.googleapis.com/css2?family=Cinzel:wght@600&family=Lato:wght@400;700&display=swap" rel="stylesheet">
<style>
  :root{
    --backdrop:#4b4b4b;
    --card-dark:#2a2a2a;
    --card-light:#ffffff;
    --gold:#cba42b;
    --ink-light:#ffffff;
    --ink-dark:#2b2b2b;
  }
  *{margin:0;padding:0;box-sizing:border-box}
  html,body{width:1200px;height:1000px;overflow:hidden}
  body{background:var(--backdrop);position:relative;font-family:'Lato',sans-serif}
  .card{position:absolute;width:584px;height:340px;overflow:hidden}
  .card-front{left:170px;top:133px;background:var(--card-dark)}
  .card-back{left:445px;top:543px;background:var(--card-light)}
  .card-back .shapes{position:absolute;inset:0}
  .brand{position:absolute;display:flex;align-items:center;gap:12px}
  .brand-mark{border-radius:50%;background:var(--gold);flex:none}
  .brand-name{font-family:'Cinzel',serif;font-weight:600;white-space:nowrap;letter-spacing:.5px}
  .card-front .brand{left:92px;top:150px}
  .card-front .brand-mark{width:30px;height:30px}
  .card-front .brand-name{font-size:27px;color:var(--ink-light)}
  .tagline{position:absolute;left:197px;top:237px;font-size:12px;font-weight:700;color:var(--ink-light);white-space:nowrap;letter-spacing:-.1px}
  .card-back .brand{left:32px;top:80px}
  .card-back .brand-mark{width:24px;height:24px}
  .card-back .brand-name{font-size:22px;color:var(--ink-dark)}
  .holder{position:absolute;left:38px;top:266px}
  .holder-name{font-family:'Cinzel',serif;font-weight:600;font-size:20px;color:var(--gold)}
  .holder-role{font-size:15px;color:var(--ink-light);margin-top:2px}
  .address{position:absolute;right:28px;top:168px;text-align:right;font-size:13.5px;color:var(--ink-light);line-height:21px}
  .contacts{position:absolute;right:28px;top:224px;list-style:none;font-size:13px;color:var(--ink-light)}
  .contacts li{display:flex;justify-content:flex-end;align-items:center;gap:8px;height:22.7px}
  .contacts svg{width:15px;height:15px;flex:none}
</style>
</head>
<body>

<section class="card card-front" aria-label="Business card front">
  <div class="brand">
    <span class="brand-mark"></span>
    <span class="brand-name">BOVENCO GLOBAL PTE. LTD.</span>
  </div>
  <p class="tagline">Lightings | Cables Terminations | Junction Box Customisation</p>
</section>

<section class="card card-back" aria-label="Business card back">
  <svg class="shapes" viewBox="0 0 584 340" preserveAspectRatio="none" aria-hidden="true">
    <path d="M0,170 C110,222 290,222 445,120 C340,200 160,238 0,216 Z" fill="var(--gold)"/>
    <path d="M0,238 C190,250 400,170 584,0 L584,340 L0,340 Z" fill="var(--card-dark)"/>
  </svg>
  <div class="brand">
    <span class="brand-mark"></span>
    <span class="brand-name">BOVENCO GLOBAL PTE. LTD.</span>
  </div>
  <div class="holder">
    <p class="holder-name">DANIEL REYES</p>
    <p class="holder-role">Director</p>
  </div>
  <p class="address">Opposite Harbour Plaza,<br>Keppel Quay, Singapore 5678</p>
  <ul class="contacts">
    <li>123 555 0142
      <svg viewBox="0 0 16 16" aria-label="Phone"><path d="M4 1.5l2.3 3-1.4 1.6c.8 1.9 2.4 3.5 4.3 4.3l1.6-1.4 3 2.3-1.3 2.6C7.2 14 2 8.8 1.5 3z" fill="var(--gold)"/></svg></li>
    <li>123 555 0142
      <svg viewBox="0 0 16 16" aria-label="Fax"><rect x="4" y="1.5" width="8" height="4" fill="var(--gold)"/><rect x="1.5" y="6" width="13" height="6" rx="1" fill="var(--gold)"/><rect x="4" y="10" width="8" height="4.5" fill="var(--gold)" stroke="var(--card-dark)" stroke-width="1"/></svg></li>
    <li>daniel.r@bovenco.com.sg
      <svg viewBox="0 0 16 16" aria-label="Email"><rect x="1" y="3.5" width="14" height="9.5" fill="var(--gold)"/><path d="M1 3.5l7 5 7-5" fill="none" stroke="var(--card-dark)" stroke-width="1.2"/></svg></li>
    <li>www.bovenco.com.sg
      <svg viewBox="0 0 16 16" aria-label="Website"><circle cx="8" cy="8" r="6.5" fill="none" stroke="var(--gold)" stroke-width="1.5"/><path d="M1.5 8h13M8 1.5c-3 3.5-3 9.5 0 13M8 1.5c3 3.5 3 9.5 0 13" fill="none" stroke="var(--gold)" stroke-width="1.1"/></svg></li>
  </ul>
</section>

</body>
</html>
```